Autora necesita un cover para su nuevo libro acerca de empoderamiento femenino*

Diseño de cover para libro digital sobre empoderamiento femenino.

El título del libro es: "Las 7 Raíces del Alma Luminosa"
Subtítulo: Se una mujer decidida, segura y satisfecha

Autora: Rosaura Beltrán

Target Market(s)

Mujeres

Font styles to use
Sans Serif

Requirements
Must have
• El título del libro es: "Las 7 Raíces del Alma Luminosa"

Autora: Rosaura Beltrán
Should not have
• Sin imágenes

```html
<!DOCTYPE html>
<html lang="es">
<head>
<meta charset="utf-8">
<title>Las 7 Raíces del Alma Luminosa — Rosaura Beltrán</title>
<link rel="stylesheet" href="https://fonts.googleapis.com/css2?family=Abril+Fatface&family=Cinzel:wght@400&family=Montserrat:wght@700&display=swap">
<style>
  :root {
    --stage: #e6e6e6;
    --cover-pink: #d04b70;
    --title-cream: #f4efec;
    --ink: #111111;
    --tone-rust: #8e4427;
    --tone-brown: #7c4b47;
    --tone-sand: #d4875e;
    --tone-mustard: #e0a832;
    --tone-teal: #0e4c66;
    --tone-forest: #032e31;
    --tone-skin: #e6bcac;
  }
  html, body {
    margin: 0;
    padding: 0;
    width: 1200px;
    height: 800px;
    overflow: hidden;
    background: var(--stage);
  }
  .book-cover {
    position: absolute;
    left: 370px;
    top: 50px;
    width: 459px;
    height: 700px;
    background: var(--cover-pink);
    overflow: hidden;
  }
  .cover-art {
    position: absolute;
    left: 0;
    top: 217px;
    width: 100%;
    height: 483px;
    display: block;
  }
  .book-title {
    position: absolute;
    top: 20px;
    left: 0;
    width: 100%;
    margin: 0;
    text-align: center;
    font-family: "Abril Fatface", "Playfair Display", serif;
    font-weight: 400;
    color: var(--title-cream);
    text-transform: uppercase;
    line-height: 0.98;
    letter-spacing: 0.01em;
  }
  .book-title .line { display: block; }
  .book-title .line-article { font-size: 40px; }
  .book-title .line-number { font-size: 62px; }
  .book-title .numeral { font-size: 86px; vertical-align: -6px; margin-right: 6px; }
  .book-title .line-middle { font-size: 62px; }
  .book-title .line-last { font-size: 54px; }
  .book-subtitle {
    position: absolute;
    top: 540px;
    left: 0;
    width: 100%;
    margin: 0;
    text-align: center;
    font-family: "Cinzel", "Times New Roman", serif;
    font-weight: 400;
    font-size: 24px;
    line-height: 1.3;
    color: var(--ink);
    text-transform: uppercase;
  }
  .book-author {
    position: absolute;
    top: 656px;
    left: 0;
    width: 100%;
    margin: 0;
    text-align: center;
    font-family: "Montserrat", "Helvetica", sans-serif;
    font-weight: 700;
    font-size: 24px;
    letter-spacing: 0.22em;
    color: var(--ink);
  }
</style>
</head>
<body>
  <main class="book-cover">
    <svg class="cover-art" viewBox="0 0 459 483" preserveAspectRatio="none"
         role="img" aria-label="Ilustración de cinco mujeres de perfil, con distintos tonos de piel y cabello, mirando a la izquierda">
      <defs>
        <linearGradient id="art-tones" x1="0" y1="0" x2="1" y2="0">
          <stop offset="0" stop-color="var(--tone-rust)"/>
          <stop offset="0.2" stop-color="var(--tone-brown)"/>
          <stop offset="0.35" stop-color="var(--tone-sand)"/>
          <stop offset="0.5" stop-color="var(--tone-mustard)"/>
          <stop offset="0.65" stop-color="var(--tone-teal)"/>
          <stop offset="0.85" stop-color="var(--tone-forest)"/>
          <stop offset="1" stop-color="var(--tone-skin)"/>
        </linearGradient>
        <linearGradient id="art-fade" x1="0" y1="0" x2="0" y2="1">
          <stop offset="0" stop-color="var(--cover-pink)" stop-opacity="1"/>
          <stop offset="0.25" stop-color="var(--cover-pink)" stop-opacity="0"/>
        </linearGradient>
      </defs>
      <rect x="0" y="0" width="459" height="483" fill="url(#art-tones)"/>
      <rect x="0" y="0" width="459" height="483" fill="url(#art-fade)"/>
    </svg>

    <h1 class="book-title">
      <span class="line line-article">Las</span>
      <span class="line line-number"><span class="numeral">7</span>Raíces</span>
      <span class="line line-middle">del Alma</span>
      <span class="line line-last">Luminosa</span>
    </h1>

    <p class="book-subtitle">Se una mujer decidida,<br>segura y satisfecha</p>

    <p class="book-author">Rosaura Beltrán</p>
  </main>
</body>
</html>
```